Velmorique needs a elegant mystical business card design

The theme of Velmorique is centered on Kemetic/Ancient Egyptian Spirituality. My business sells handmade scented candles, mystic oils, body sprays, tarot readings and more. I would like my business card to reflect an elegant and mystical look. Hieroglyphs around the borders would be a cool idea. Also, the main colors I am working with is Black and Gold= colors of royalty. Black background. The business card will be double sided. The back will have the logo, and the front will have the basic information (ie name, title, business, phone, email, website, etc..)

Target Market(s)

The target market are people into metaphysics, holistic healing, ancient Egyptian culture, aromatherapy, occult science, and the esoteric.

Industry/Entity Type

Business

Contact Information for Business Card

Name: Marlonda T. Pruitt
Title: Owner
Business: VELMORIQUE
Phone: 917.302.4417
Website: www.Velmorique.net
Facebook, Instagram, and twitter icons

Font styles to use
Serif
Decorative

Requirements
Must have
• My logo, and website.
Nice to have
• Ancient Egyptian hieroglyphs, Elegant designs around the border, or encircling the logo.

```html
<!DOCTYPE html>
<html lang="en">
<head>
<meta charset="utf-8">
<title>Velmorique Business Card</title>
<link href="https://fonts.googleapis.com/css2?family=Cinzel:wght@500&family=Noto+Serif:wght@400;700&family=UnifrakturCook:wght@700&display=swap" rel="stylesheet">
<style>
  :root {
    --backdrop: #3a3633;
    --card-black: #070707;
    --gold: #c9a24f;
    --gold-light: #f2d98a;
    --gold-deep: #8a6424;
    --band-light: #e7a463;
    --band-dark: #b8692e;
  }
  * { margin: 0; padding: 0; box-sizing: border-box; }
  html, body { width: 1200px; height: 1200px; overflow: hidden; }
  body {
    background: var(--backdrop);
    position: relative;
    font-family: "Noto Serif", Georgia, serif;
    color: var(--gold);
  }
  .card {
    position: absolute;
    width: 784px;
    height: 452px;
    background: var(--card-black);
    box-shadow: 0 6px 18px rgba(0,0,0,.55);
    overflow: hidden;
  }
  .card--logo { left: 104px; top: 134px; }
  .card--info { left: 294px; top: 630px; background: radial-gradient(ellipse at 50% 70%, #151312 0%, var(--card-black) 70%); }

  .gold-rule {
    position: absolute;
    height: 8px;
    background: linear-gradient(90deg, var(--gold-deep), var(--gold-light) 45%, var(--gold) 70%, rgba(201,162,79,0));
  }
  .card--logo .gold-rule { top: 0; left: 0; width: 680px; }
  .card--info .gold-rule--top { top: 0; left: 0; width: 720px; }
  .card--info .gold-rule--bottom {
    bottom: 0; left: 70px; width: 660px;
    background: linear-gradient(90deg, rgba(201,162,79,0), var(--gold) 20%, var(--gold-light) 55%, var(--gold) 80%, rgba(201,162,79,0));
  }

  .brand-mark {
    position: absolute;
    left: 0; right: 0;
    text-align: center;
    font-family: "Cinzel", "Times New Roman", serif;
    font-weight: 500;
    color: var(--gold);
    letter-spacing: .08em;
  }
  .card--logo .brand-mark { top: 92px; font-size: 34px; }
  .card--info .brand-mark { top: 72px; font-size: 20px; }

  .web-line {
    position: absolute; left: 0; right: 0; text-align: center;
    font-size: 26px; color: var(--gold);
  }
  .card--logo .web-line { top: 208px; }
  .globe { display: inline-block; vertical-align: -2px; margin-right: 6px; }

  .glyph-band {
    position: absolute; left: 0; bottom: 0; width: 100%; height: 196px;
    background: linear-gradient(180deg, var(--band-light), var(--band-dark) 55%, var(--band-light));
  }

  .contact { position: absolute; left: 0; right: 0; top: 162px; text-align: center; }
  .contact__name { font-weight: 700; font-size: 22px; color: var(--gold); letter-spacing: .02em; }
  .contact__name .initial { font-family: "UnifrakturCook", "Noto Serif", serif; font-size: 30px; }
  .contact__title { font-size: 22px; margin-top: 2px; color: #b89550; }
  .contact__business { font-size: 24px; margin-top: 14px; color: var(--gold); }
  .contact__phone { font-size: 24px; margin-top: 2px; color: var(--gold); }
  .contact__web { font-size: 23px; margin-top: 8px; color: var(--gold); }
  .social { display: flex; justify-content: center; gap: 52px; margin-top: 14px; }
  .social__dot { width: 20px; height: 20px; border-radius: 50%; background: var(--gold); }
</style>
</head>
<body>

  <section class="card card--logo">
    <div class="gold-rule"></div>
    <div class="brand-mark">VELMORIQUE</div>
    <div class="web-line">
      <svg class="globe" width="18" height="18" viewBox="0 0 18 18" fill="none" stroke="#c9a24f" stroke-width="1.4"><circle cx="9" cy="9" r="7.5"/><ellipse cx="9" cy="9" rx="3.2" ry="7.5"/><line x1="1.5" y1="9" x2="16.5" y2="9"/><line x1="3" y1="5" x2="15" y2="5"/><line x1="3" y1="13" x2="15" y2="13"/></svg>www.Velmorique.net
    </div>
    <div class="glyph-band" role="img" aria-label="Band of carved ancient Egyptian hieroglyphs on warm orange sandstone"></div>
  </section>

  <section class="card card--info">
    <div class="gold-rule gold-rule--top"></div>
    <div class="brand-mark">VELMORIQUE</div>
    <div class="contact">
      <div class="contact__name"><span class="initial">M</span>arlonda&nbsp;&nbsp;<span class="initial">T</span>.&nbsp;&nbsp;<span class="initial">P</span>ruitt</div>
      <div class="contact__title">(Owner)</div>
      <div class="contact__business">VELMORIQUE</div>
      <div class="contact__phone">
        <svg width="12" height="20" viewBox="0 0 12 20" fill="none" stroke="#c9a24f" stroke-width="1.6" style="vertical-align:-2px"><rect x="1" y="1" width="10" height="18" rx="2"/><line x1="4.5" y1="16" x2="7.5" y2="16"/></svg>
        917.302.4417
      </div>
      <div class="contact__web">
        <svg class="globe" width="18" height="18" viewBox="0 0 18 18" fill="none" stroke="#c9a24f" stroke-width="1.4"><circle cx="9" cy="9" r="7.5"/><ellipse cx="9" cy="9" rx="3.2" ry="7.5"/><line x1="1.5" y1="9" x2="16.5" y2="9"/><line x1="3" y1="5" x2="15" y2="5"/><line x1="3" y1="13" x2="15" y2="13"/></svg>www.Velmorique.net
      </div>
      <div class="social">
        <span class="social__dot"></span>
        <span class="social__dot"></span>
        <span class="social__dot"></span>
      </div>
    </div>
    <div class="gold-rule gold-rule--bottom"></div>
  </section>

</body>
</html>
```